Simple, High-Class Web Design Wanted - Motivational Speakers Site

1. Full Brief/Request & Specs outlined on following video -
http://clipvarnish-demo.com/watch/tRbWlKpZgQ

2. Use colours, images as you feel suits objective (we are happy to pay up to US$30 for any good images but must have licence/permission).

3. Layout probably similar to existing site - www.quillhavenorators.com.au / http://quillhavenorators.com.au/contact.php

4. Must Be Able to Coded for MOBILE-FRIENDLINESS & WordPress friendly Ideal.

5. This is the first, small job of many we/graphic design jobs. If suits, winning designer may be offered all future work direct.

Thanks & look forward to your design. Doug.

Target Market(s)

corporates - high end

Number of Pages Required

2 page

Font styles to use
Sans Serif

Requirements
Must have
• Classy professional look
Nice to have
• all in Video in brief
Should not have
• too many images / new images I haven't approved

```html
<!DOCTYPE html>
<html lang="en">
<head>
<meta charset="utf-8">
<title>Quillhaven Orators – Find The Perfect Speaker</title>
<link href="https://fonts.googleapis.com/css2?family=Open+Sans:wght@400;600;700;800&display=swap" rel="stylesheet">
<style>
:root{
  --maroon:#7e1b3b;
  --maroon-dark:#5f1229;
  --ink:#333333;
  --muted:#6f6f6f;
  --paper:#ffffff;
  --band:#e8e6e2;
  --hero:#cfcac6;
  --footer:#2a2a2a;
  --footer-deep:#1d1d1d;
  --line:#d7d3ce;
}
*{box-sizing:border-box;margin:0;padding:0}
html,body{width:1200px;height:2580px;overflow:hidden}
body{font-family:"Open Sans",Arial,sans-serif;color:var(--ink);background:var(--paper);font-size:14px;position:relative}
.wrap{width:820px;margin:0 auto;position:relative}

/* top banner */
.topbar{background:var(--maroon);height:120px;text-align:center;color:#fff;padding-top:14px}
.topbar h1{font-size:38px;font-weight:800;letter-spacing:.5px}
.topbar .tag{position:absolute;right:190px;top:66px;font-size:24px;font-weight:600}

/* hero */
.hero{height:420px;background:linear-gradient(180deg,#d7d2ce 0%,#bdb6b1 100%);position:relative;border-bottom:6px solid var(--maroon)}
.hero .pitch{position:absolute;left:285px;top:40px;width:380px;color:#222}
.hero .pitch h2{font-size:21px;font-weight:700;line-height:1.3}
.btn{display:inline-block;background:var(--maroon);color:#fff;font-weight:600;font-size:15px;padding:9px 22px}
.hero .btn{margin-top:28px}
.hero .portrait{position:absolute;left:715px;top:18px;width:300px;height:396px;background:linear-gradient(180deg,#8a8f99,#2f3642)}

/* search */
.search{display:flex;margin-top:22px;height:32px}
.search .field{flex:1;border:1px solid var(--line);font-size:13px;color:#999;padding:6px 10px}
.search .go{width:70px;background:var(--maroon);display:flex;align-items:center;justify-content:center}

.section-head{display:flex;align-items:center;justify-content:space-between;border-bottom:2px solid var(--line);margin-top:28px;padding-bottom:8px}
.section-head h3{font-size:15px;font-weight:700;text-transform:uppercase;color:var(--ink);border-bottom:2px solid var(--maroon);margin-bottom:-10px;padding-bottom:8px}
.arrows{display:flex;gap:4px}
.arrows span{width:20px;height:20px;background:var(--maroon);display:flex;align-items:center;justify-content:center}

/* speakers */
.speakers{background:var(--band);height:260px;margin-top:20px;padding-top:26px}
.speakers .row{display:flex;justify-content:space-between}
.speaker{width:196px;height:200px;border:5px solid #fff;box-shadow:0 1px 3px rgba(0,0,0,.2)}
.s1{background:linear-gradient(160deg,#3c5a86,#17243a)}
.s2{background:linear-gradient(160deg,#8a8f96,#353a42)}
.s3{background:linear-gradient(160deg,#6f6f73,#22252b)}
.s4{background:linear-gradient(160deg,#b7b9bd,#4f5257)}

/* about */
.about p{font-size:12.5px;color:var(--muted);line-height:1.6;margin-top:18px}
.features{display:flex;justify-content:space-around;margin-top:30px;text-align:center}
.feature{width:170px}
.feature svg{display:block;margin:0 auto 8px}
.feature h4{font-size:13px;font-weight:700}
.feature small{display:block;font-size:11px;color:var(--muted);line-height:1.4;margin-top:2px}
.contact-lines{margin-top:30px;font-size:12px;color:var(--muted)}
.contact-lines div{display:flex;align-items:center;gap:8px;margin-bottom:8px}
.about .btn{margin-top:18px;font-size:13px;padding:8px 20px}

/* video */
.video{height:380px;margin-top:36px;background:linear-gradient(180deg,#3b3a3c 0%,#6d5e55 55%,#2c2a2b 100%);position:relative}
.player{position:absolute;left:395px;top:20px;width:500px;height:270px;background:linear-gradient(180deg,#8f9aa6,#4b5563);border:4px solid #fff}
.player .bar{position:absolute;left:0;right:0;bottom:0;height:22px;background:rgba(0,0,0,.75);display:flex;align-items:center;padding:0 8px;gap:8px}
.player .bar i{flex:1;height:3px;background:#888;display:block}
.player .play{position:absolute;left:50%;top:50%;transform:translate(-50%,-50%)}
.caption{position:absolute;left:395px;top:294px;width:500px;background:var(--maroon);color:#fff;font-size:18px;font-weight:600;text-align:center;padding:7px 0}

/* notes and news */
.cols{display:flex;justify-content:space-between;margin-top:26px}
.col{width:395px}
.col .section-head{margin-top:0}
.note-box{margin-top:16px;font-size:11.5px;color:var(--muted);line-height:1.55}
.note-box div{display:flex;gap:8px;margin-bottom:10px}
.note-box div b{width:10px;height:10px;background:var(--maroon);flex:none;margin-top:4px}
.note-box .btn{margin-top:8px;font-size:12px;padding:7px 16px}
.news{display:flex;gap:12px;margin-top:16px}
.news .thumb{width:150px;height:95px;flex:none}
.t1{background:linear-gradient(160deg,#a86a4f,#4a2c22)}
.t2{background:linear-gradient(160deg,#7b8794,#2e343c)}
.news h5{font-size:13px;font-weight:600}
.news .meta{font-size:10px;color:var(--maroon);margin:4px 0}
.news p{font-size:11px;color:var(--muted);line-height:1.45}

/* footer */
.footer{position:absolute;left:0;top:2340px;width:1200px;height:190px;background:var(--footer);color:#ddd}
.footer .wrap{display:flex;justify-content:space-between;padding-top:20px}
.footer h6{font-size:15px;font-weight:700;color:#fff;text-transform:uppercase;margin-bottom:14px}
.footer .fc{width:250px;font-size:11px;line-height:1.7}
.footer .fc div{display:flex;gap:8px;align-items:flex-start;margin-bottom:4px}
.footer input{width:210px}
.footer .sub-field{width:200px;height:24px;background:#3c3c3c;border:1px solid #555;font-size:10px;color:#999;padding:4px 8px;margin:6px 0}
.footer .sub-btn{display:inline-block;background:var(--maroon);color:#fff;font-size:10px;font-weight:600;padding:4px 14px}
.gallery{display:grid;grid-template-columns:repeat(3,66px);gap:6px}
.gallery span{height:46px;background:linear-gradient(160deg,#8a6d55,#3b2f28)}
.gallery span:nth-child(even){background:linear-gradient(160deg,#6f7884,#2c3138)}
.legal{position:absolute;left:0;top:2530px;width:1200px;height:50px;background:var(--footer-deep);color:#aaa;font-size:11px}
.legal .wrap{padding-top:17px}
</style>
</head>
<body>

<header class="topbar">
  <h1>Find The Perfect Speaker For Your Next Event Here...</h1>
  <span class="tag">Free Industry Service</span>
</header>

<section class="hero">
  <div class="pitch">
    <h2>Looking for a Top Motivational or Guest Speakers MC or Industry Expert to “WOW” Your Next Event?</h2>
    <span class="btn">Find Them now</span>
  </div>
  <div class="portrait" role="img" aria-label="Photo of a featured speaker in a suit"></div>
</section>

<main class="wrap">
  <div class="search">
    <div class="field">Search for speakers...</div>
    <div class="go"><svg width="16" height="16" viewBox="0 0 16 16"><circle cx="6.5" cy="6.5" r="5" fill="none" stroke="#fff" stroke-width="2"/><line x1="10.5" y1="10.5" x2="15" y2="15" stroke="#fff" stroke-width="2"/></svg></div>
  </div>

  <div class="section-head">
    <h3>Australian Speakers</h3>
    <div class="arrows">
      <span><svg width="8" height="10"><path d="M7 0L1 5l6 5z" fill="#fff"/></svg></span>
      <span><svg width="8" height="10"><path d="M1 0l6 5-6 5z" fill="#fff"/></svg></span>
    </div>
  </div>
</main>

<section class="speakers">
  <div class="wrap row">
    <div class="speaker s1" role="img" aria-label="Speaker photo presenting on stage"></div>
    <div class="speaker s2" role="img" aria-label="Speaker portrait photo"></div>
    <div class="speaker s3" role="img" aria-label="Speaker portrait photo"></div>
    <div class="speaker s4" role="img" aria-label="Speaker portrait photo"></div>
  </div>
</section>

<section class="wrap about">
  <div class="section-head"><h3>About Us</h3></div>
  <p>Quillhaven Orators is a free industry service designed to help people looking for speakers and presenters find and book the right voice for their conference, gala or team event. Suggestions are given for Australian conference speakers from all walks of life, and our consultants source presenters for a number of years across a variety of sectors and budgets. Tell us a little about your event and the type of presenter you are after and we will come back to you with a short list of ideas to consider.</p>
  <div class="features">
    <div class="feature">
      <svg width="48" height="48" viewBox="0 0 48 48"><circle cx="24" cy="14" r="9" fill="var(--maroon)"/><path d="M8 46c0-10 7-17 16-17s16 7 16 17z" fill="var(--maroon)"/></svg>
      <h4>Topic/Style</h4><small>Motivational, Entertaining, Inspirational, Humour</small>
    </div>
    <div class="feature">
      <svg width="48" height="48" viewBox="0 0 48 48"><rect x="4" y="14" width="40" height="28" rx="3" fill="var(--maroon)"/><rect x="17" y="6" width="14" height="10" rx="2" fill="none" stroke="var(--maroon)" stroke-width="3"/></svg>
      <h4>Topic Area</h4><small>Team Building, Leadership, Resilience, Health &amp; Sales</small>
    </div>
    <div class="feature">
      <svg width="48" height="48" viewBox="0 0 48 48"><circle cx="24" cy="28" r="17" fill="var(--maroon)"/><rect x="18" y="3" width="12" height="8" fill="var(--maroon)"/><text x="24" y="35" text-anchor="middle" font-family="Open Sans,sans-serif" font-weight="700" font-size="18" fill="#fff">$</text></svg>
      <h4>Approximate Budget</h4><small>$1000, $2500, $5000, $7500+ etc</small>
    </div>
    <div class="feature">
      <svg width="48" height="48" viewBox="0 0 48 48"><path d="M24 46S8 28 8 18a16 16 0 0 1 32 0c0 10-16 28-16 28z" fill="var(--maroon)"/><circle cx="24" cy="18" r="6" fill="#fff"/></svg>
      <h4>Location</h4><small>Sydney, Melbourne, Brisbane, Perth, Adelaide etc</small>
    </div>
  </div>
  <p>Once we have an idea of your event we will be happy to send you some speaker suggestions to consider, with no obligation and no cost to you at all.</p>
  <div class="contact-lines">
    <div><svg width="14" height="10"><rect x="0.5" y="0.5" width="13" height="9" fill="none" stroke="var(--maroon)"/><path d="M1 1l6 5 6-5" fill="none" stroke="var(--maroon)"/></svg>hello@quillhavenorators.com.au</div>
    <div><svg width="12" height="14" viewBox="0 0 12 14"><path d="M2 1h3l1 3-2 1a7 7 0 0 0 3 4l1-2 3 1v3c0 1-1 2-2 2C5 13 0 8 0 3c0-1 1-2 2-2z" fill="var(--maroon)"/></svg>1300 555 014</div>
  </div>
  <span class="btn">Quick Online Contact Form</span>
</section>

<section class="video">
  <div class="player" role="img" aria-label="Video still of a speaker presenting">
    <svg class="play" width="60" height="60" viewBox="0 0 60 60"><circle cx="30" cy="30" r="28" fill="rgba(0,0,0,.45)"/><path d="M24 18l18 12-18 12z" fill="#fff"/></svg>
    <div class="bar"><svg width="8" height="10"><path d="M0 0l8 5-8 5z" fill="#fff"/></svg><i></i></div>
  </div>
  <div class="caption">I Want to Make Our Event a Great Success</div>
</section>

<section class="wrap cols">
  <div class="col">
    <div class="section-head"><h3>Please Note:</h3></div>
    <div class="note-box">
      <div><b></b><span>Any information you provide will NOT ever be sent on to any third party agents or listing sites.</span></div>
      <div><b></b><span>Most dates are fixed and all appearances are confirmed directly with the individual speakers. We recommend you offer a range of dates where possible so we can suggest more speakers.</span></div>
      <div><b></b><span>Please understand that while fees are listed as a guide, they can vary with travel and timing.</span></div>
      <span class="btn">Quick Online Contact Form</span>
    </div>
  </div>
  <div class="col">
    <div class="section-head"><h3>Recent News:</h3></div>
    <div class="news">
      <div class="thumb t1" role="img" aria-label="Photo of an event audience"></div>
      <div><h5>Exception not occurred, updated</h5><div class="meta">Admin · 03 Sep, 2015</div><p>Our team has added new conference speakers to our list this month, with fresh ideas on leadership, growth and resilience.</p></div>
    </div>
    <div class="news">
      <div class="thumb t2" role="img" aria-label="Photo of a speaker at a lectern"></div>
      <div><h5>Simple point occurred</h5><div class="meta">Admin · 03 Sep, 2015</div><p>Simple planning tips to help your event run smoothly from first booking to final applause.</p></div>
    </div>
  </div>
</section>

<footer class="footer">
  <div class="wrap">
    <div class="fc">
      <h6>Contact Us</h6>
      <div><svg width="10" height="14" viewBox="0 0 10 14"><path d="M5 14S0 8 0 5a5 5 0 0 1 10 0c0 3-5 9-5 9z" fill="var(--maroon)"/></svg><span>PO Box 417, Ferndale Junction<br>NSW 2099</span></div>
      <div><svg width="10" height="12" viewBox="0 0 12 14"><path d="M2 1h3l1 3-2 1a7 7 0 0 0 3 4l1-2 3 1v3c0 1-1 2-2 2C5 13 0 8 0 3c0-1 1-2 2-2z" fill="var(--maroon)"/></svg><span>1300 555 014</span></div>
      <div><svg width="10" height="12" viewBox="0 0 12 14"><path d="M2 1h3l1 3-2 1a7 7 0 0 0 3 4l1-2 3 1v3c0 1-1 2-2 2C5 13 0 8 0 3c0-1 1-2 2-2z" fill="var(--maroon)"/></svg><span>02 5550 1472</span></div>
      <div><svg width="12" height="9"><rect x="0.5" y="0.5" width="11" height="8" fill="none" stroke="var(--maroon)"/></svg><span>hello@quillhavenorators.com.au</span></div>
    </div>
    <div class="fc">
      <h6>Newsletter</h6>
      <span>Subscribe to our newsletter</span>
      <div class="sub-field">Enter address</div>
      <span class="sub-btn">SUBSCRIBE</span>
    </div>
    <div class="fc">
      <h6>Gallery</h6>
      <div class="gallery" role="img" aria-label="Gallery of event photos">
        <span></span><span></span><span></span><span></span><span></span><span></span>
      </div>
    </div>
  </div>
</footer>
<div class="legal"><div class="wrap">© Copyright Quillhaven Orators</div></div>

</body>
</html>
```